Menu Design

I am seeking a designer to re create our menu for our stores.

I have attached our current menu and would I have also attached some menus I like for inspiration

The menu is to be split across 2 pages, Please present the menu of 2 horizontal a4 pages and our in house designer will adjust the final PSD file to suit our stores different configurations.

Kindest Regards

The text for the menu is as follows

BASE SHAKE (Choc, Strawberry, Vanilla, Banana) (Reg $4.95 Large $5.95)

ADD-ON'S

Protein $2
Superfruit $2
Coconut Water $2
Chia Seeds $1
Energiser $1
Fat-burner $1
L-Carnitine $1
Glutamine $1

ACTIVE LIFESTYLE SMOOTHIES (Available in Chocolate, Strawberry, Vanilla, Banana) (Reg $6.95 Large $7.95)

Kick Start (Muscle, Weight Loss)
Protein, Protein Frozen Yoghurt, Caffeine, Water, Ice

Recovery (Muscle, Weight Loss)
Protein, Protein Frozen Yoghurt, L-Glutamine, Viamin C Powder, Water, Ice

Shredder (Weight Loss)
Protein, Protein Frozen Yoghurt, L-Carnitine, Thermogenic, Vitamin C Powder, Chia Seeds, Water, Ice

Muscle Maker (Muscle)
Protein, Protein Frozen Yoghurt, Full Cream Milk, Dextrose, Flaxseed Oil, Creatine Monohydrate

SUPER SMOOTHIES (Reg $8.95 Large $9.95)

Honey Nutter (Favourite, Muscle, Weight Loss)
Chocolate Protein, Natural Peanut Butter, Chia Seeds, Manuka Honey, Cocoa Nibs, Water, Ice

Choc-Mint Powerhouse (Muscle, Weight Loss)
Chocolate Protein, Mint, Natural Peanut Butter, Walnuts, Almonds, Chia Seeds, Manuka Honey, Water, Ice

Forever Energy (Favourite, Muscle, Weight Loss, Vitality)
Vanilla Protein, Almond Flakes, Avocado, Chia Seeds, Banana, Dates, Cacao Nibs, Acai Powder, Coconut Water, Ice

Cardio Berry- Bomb (Muscle, Weight Loss)
Vanilla Protein, Banana, Mixed Berries, Chia Seeds, Antioxidant Mix (pomegranate, maqui, acai, elderflower, green tea powder), Coconut Water, Ice\

Toxin Cleanser (Muscle, Weight Loss, Vitality)
Vanilla Protein, Kale, Pear, Banana, Pineapple, Chia Seeds, Water, Ice

Morning Glory (Muscle, Weight Loss, Vitality)
Vanilla Protein, Blueberries, Goji Berries, Walnuts, Manuka Honey, Avocado, Coconut Water, Ice

SUPERFRUIT SMOOTHIES (Reg $8.95 Large $9.95)

Tropical Tonic (Muscle, Weight Loss, Vitality)
Vanilla Protein, Passionfruit, Almonds, Mango, Avocado, Manuka Honey, Chia Seeds, Coconut Water, Ice

Peach Pick-Me-Up (Muscle, Weight Loss, Vitality)
Vanilla Protein, Peach, Banana, Kale, Pear, Almonds, Chia Seeds, Coconut Water, Ice

Mango Madness (Favourite, Muscle, Weight Loss, Vitality)
Vanilla Protein, Mango, Almond Flakes, Manuka Honey, Ice, Chia Seeds, Water, Ice

Banana Bliss (Favourite, Muscle, Weight Loss)
Banana Protein, Banana, Cacao Nibs, Manuka Honey, Chia Seeds, Walnuts, Cinnamon, Chia Seeds, Water, Ice

Berry Sweet (Favourite, Muscle, Weight Loss)
Strawberry Protein, Mixed Berries, Acai Powder, Goji Berries, Cranberries, Shredded Coconut, Water, Ice

VEGAN SMOOTHIES (Reg $8.95 Large $9.95)

Acai (Vitality, Weight Loss, Dairy Free, Gluten Free)
Acai Powder, Banana, Chia Seeds, Goji Berries, Cranberries, Coconut Water, Ice

Energiser (Vitality, Weight Loss, Dairy Free, Gluten Free)
Raw Energy Powder (traditional herbs, slow-release ancient seeds, and concentrated sea minerals), Acai Powder, Blueberries, Avocado, Chia Seeds, Coconut Water, Ice

Complete Biotic (Vitality, Weight Loss, Dairy Free, Gluten Free)
Raw Pre-Probiotic Powder, Mango, Chia Seeds, Almond Flakes, Coconut Water, Ice

Vegan Vigor (Favourite, Muscle, Weight Loss, Vitality, Dairy Free, Gluten Free)
Vegetable Protein, Blueberries, Banana, Cinnamon, Walnuts, Chia Seeds, Antioxidant Mix (pomegranate, maqui, acai, elderflower, green tea powder), Coconut Water, Ice

KIDS ($3.95)

Chocolate
Low Fat Milk, Cacao Nibs, Chia Seeds

Strawberry
Low Fat Milk, Strawberries, Goji Berries

Banana
Low Fat Milk, Banana, Chia Seeds

Banana Choc
Low Fat Milk, Banana, Honey, Cacao Nibs

FROZEN YOGHURT (Up to 3 toppings- extra toppings $0.50 each)

Small $4.50
Medium $6.00
Large $7.50

PROTEIN PANCAKES (Available in Chocolate, Strawberry, Banana)

3 Stack $6.95
5 Stack $8.45
Protein Pocket $3.50

FOOD AND EXTRA'S

Acai Bowl $9.95
Protein Balls $2
Vornel Bars $4.50

Lumbra- Glo Tea $3.95
Bottled Water $2.45
Coconut Water $3.30

Target Market(s)

Our customers are both male and female 18 - 35 who have an interest in health, fitness, healthy eating and overall well being

Industry/Entity Type

House

Colors
0492cd
e567a6
ebf7f9
33a6d7
b768aa

Requirements
Must have
• must be clean and easy to read.
Nice to have
• Images of the shakes taken from the uploaded psd file

```html
<!DOCTYPE html>
<html lang="en">
<head>
<meta charset="utf-8">
<title>Smoothie Menu</title>
<link rel="stylesheet" href="https://fonts.googleapis.com/css2?family=Lobster&family=Dosis:wght@400;500;600&display=swap">
<style>
  :root {
    --paper: #f4f4f3;
    --paper-shade: #ebebea;
    --ink: #2b2b2b;
    --ink-soft: #555;
    --pink: #e12a7b;
    --purple: #7f3f98;
    --orange: #f7941d;
    --green: #7dc243;
    --teal: #7fd3d4;
    --white: #ffffff;
  }
  * { box-sizing: border-box; margin: 0; padding: 0; }
  html, body { width: 1200px; height: 848px; overflow: hidden; }
  body {
    position: relative;
    background: linear-gradient(100deg, var(--paper) 0%, var(--paper-shade) 50%, var(--paper) 100%);
    font-family: "Dosis", sans-serif;
    color: var(--ink);
  }
  .abs { position: absolute; }
  .section-title {
    position: absolute;
    font-family: "Lobster", cursive;
    font-weight: 400;
    font-size: 48px;
    line-height: 1;
    white-space: nowrap;
  }
  .section-note {
    position: absolute;
    font-size: 19px;
    font-weight: 600;
    color: var(--ink-soft);
    white-space: nowrap;
  }
  .dots { position: absolute; border-top: 3px dotted #555; height: 0; }
  .price-badge {
    position: absolute;
    z-index: 3;
    border-radius: 50%;
    color: var(--white);
    font-size: 17px;
    font-weight: 500;
    line-height: 1.2;
    display: flex;
    flex-direction: column;
    justify-content: center;
    align-items: center;
  }
  .badge-dot { position: absolute; z-index: 3; border-radius: 50%; }

  /* base shake */
  .base-title { left: 40px; top: 32px; color: var(--pink); }
  .addons-title { left: 40px; top: 151px; font-size: 21px; font-weight: 500; }
  .addon { position: absolute; font-size: 16.5px; font-weight: 500; }
  .shake-visual {
    z-index: 1;
    left: 350px; top: 36px; width: 225px; height: 256px;
    border-radius: 40% 40% 30% 30%;
    background: radial-gradient(circle at 50% 45%, #c9a7c9 0%, #e6d8e6 45%, rgba(244,244,243,0) 72%);
  }
  .good-stuff {
    left: 110px; top: 286px; width: 430px; height: 104px;
    border-radius: 50px;
    background: radial-gradient(ellipse at center, rgba(127,211,212,0.35) 0%, rgba(127,211,212,0) 70%);
  }

  /* menu items */
  .menu-item { position: absolute; }
  .item-name {
    font-family: "Lobster", cursive;
    font-size: 28px;
    line-height: 1;
  }
  .item-tags { font-size: 19.5px; font-weight: 600; color: #444; }
  .item-desc { font-size: 15px; line-height: 19px; font-weight: 500; text-align: justify; margin-top: 3px; }

  /* active lifestyle */
  .active-title { left: 40px; top: 416px; color: var(--purple); }
  .active { left: 40px; width: 437px; }
  .active .item-name { color: var(--purple); }

  /* super smoothies */
  .super-title { left: 620px; top: 34px; color: var(--orange); }
  .super { left: 618px; width: 542px; }
  .super .item-name { color: var(--orange); }

  /* kids */
  .kids-blob { left: 0; top: 0; }
  .kids-title { left: 734px; top: 606px; color: var(--white); }
  .kids-price { left: 943px; top: 642px; font-family: "Lobster", cursive; color: var(--white); font-size: 24px; }
  .kids-dots { left: 630px; top: 680px; width: 438px; border-top-color: var(--white); }
  .kid { position: absolute; color: var(--white); }
  .kid .item-desc { font-size: 15.5px; margin-top: 6px; text-align: left; }
</style>
</head>
<body>

  <!-- Base shake -->
  <h2 class="section-title base-title">Base Shake</h2>
  <p class="section-note" style="left:40px;top:88px;">(Choc, Strawberry, Vanilla, Banana)</p>
  <div class="dots" style="left:40px;top:128px;width:268px;"></div>
  <div class="badge-dot" style="left:302px;top:122px;width:12px;height:12px;background:var(--pink);"></div>
  <div class="price-badge" style="left:302px;top:104px;width:92px;height:92px;background:var(--pink);">
    <span>Reg $4.95</span><span>Large $5.95</span>
  </div>

  <p class="addons-title abs">+ ADD-ON'S</p>
  <span class="addon" style="left:40px;top:184px;">Protein</span><span class="addon" style="left:145px;top:184px;">$2</span>
  <span class="addon" style="left:40px;top:208px;">Superfruit</span><span class="addon" style="left:145px;top:208px;">$2</span>
  <span class="addon" style="left:40px;top:232px;">Coconut Water</span><span class="addon" style="left:145px;top:232px;">$2</span>
  <span class="addon" style="left:40px;top:257px;">Chia Seeds</span><span class="addon" style="left:148px;top:257px;">$1</span>
  <span class="addon" style="left:186px;top:184px;">Energiser</span><span class="addon" style="left:283px;top:184px;">$1</span>
  <span class="addon" style="left:186px;top:208px;">Fat-burner</span><span class="addon" style="left:283px;top:208px;">$1</span>
  <span class="addon" style="left:186px;top:232px;">L-Carnitine</span><span class="addon" style="left:283px;top:232px;">$1</span>
  <span class="addon" style="left:186px;top:257px;">Glutamine</span><span class="addon" style="left:283px;top:257px;">$1</span>

  <div class="abs shake-visual" role="img" aria-label="Two smoothie cups with bananas, strawberries, blueberries and raspberries"></div>
  <div class="abs good-stuff" role="img" aria-label="Hand-lettered slogan: Full of Good Stuff, with sun rays"></div>

  <!-- Active lifestyle -->
  <h2 class="section-title active-title">Active Lifestyle Smoothies</h2>
  <p class="section-note" style="left:40px;top:471px;">(Available in Chocolate, Strawberry, Vanilla, Banana)</p>
  <div class="dots" style="left:40px;top:512px;width:405px;"></div>
  <div class="badge-dot" style="left:441px;top:506px;width:12px;height:12px;background:var(--purple);"></div>
  <div class="price-badge" style="left:443px;top:478px;width:94px;height:94px;background:var(--purple);">
    <span>Reg $6.95</span><span>Large $7.95</span>
  </div>

  <div class="menu-item active" style="top:530px;">
    <p><span class="item-name">Kick Start</span> <span class="item-tags">(Muscle, Weight Loss)</span></p>
    <p class="item-desc">Protein, Protein Frozen Yoghurt, Caffeine, Water, Ice</p>
  </div>
  <div class="menu-item active" style="top:595px;">
    <p><span class="item-name">Recovery</span> <span class="item-tags">(Muscle, Weight Loss)</span></p>
    <p class="item-desc">Protein, Protein Frozen Yoghurt, L-Glutamine, Viamin C Powder, Water, Ice</p>
  </div>
  <div class="menu-item active" style="top:660px;">
    <p><span class="item-name">Shredder</span> <span class="item-tags">(Weight Loss)</span></p>
    <p class="item-desc">Protein, Protein Frozen Yoghurt, L-Carnitine, Thermogenic, Vitamin C Powder, Chia Seeds, Water, Ice</p>
  </div>
  <div class="menu-item active" style="top:743px;">
    <p><span class="item-name">Muscle Maker</span> <span class="item-tags">(Muscle)</span></p>
    <p class="item-desc">Protein, Protein Frozen Yoghurt, Full Cream Milk, Dextrose, Flaxseed Oil, Creatine Monohydrate</p>
  </div>

  <!-- Super smoothies -->
  <h2 class="section-title super-title">Super Smoothies</h2>
  <div class="dots" style="left:620px;top:97px;width:448px;"></div>
  <div class="badge-dot" style="left:1064px;top:50px;width:12px;height:12px;background:var(--orange);"></div>
  <div class="price-badge" style="left:1063px;top:26px;width:100px;height:100px;background:var(--orange);">
    <span>Reg $8.95</span><span>Large $9.95</span>
  </div>

  <div class="menu-item super" style="top:115px;">
    <p><span class="item-name">Honey Nutter</span> <span class="item-tags">(Favourite, Muscle, Weight Loss)</span></p>
    <p class="item-desc">Chocolate Protein, Natural Peanut Butter, Chia Seeds, Manuka Honey, Cocoa Nibs, Water, Ice</p>
  </div>
  <div class="menu-item super" style="top:178px;">
    <p><span class="item-name">Choc-Mint Powerhouse</span> <span class="item-tags">(Muscle, Weight Loss)</span></p>
    <p class="item-desc">Chocolate Protein, Mint, Natural Peanut Butter, Walnuts, Almonds, Chia Seeds, Manuka Honey, Water, Ice</p>
  </div>
  <div class="menu-item super" style="top:262px;">
    <p><span class="item-name">Forever Energy</span> <span class="item-tags">(Favourite, Muscle, Weight Loss, Vitality)</span></p>
    <p class="item-desc">Vanilla Protein, Almond Flakes, Avocado, Chia Seeds, Banana, Dates, Cacao Nibs, Acai Powder, Coconut Water, Ice</p>
  </div>
  <div class="menu-item super" style="top:346px;">
    <p><span class="item-name">Cardio Berry-Bomb</span> <span class="item-tags">(Muscle, Weight Loss)</span></p>
    <p class="item-desc">Vanilla Protein, Banana, Mixed Berries, Chia Seeds, Antioxidant Mix (maqui, pomegranate, acai, elderflower, green tea powder), Coconut Water, Ice</p>
  </div>
  <div class="menu-item super" style="top:429px;">
    <p><span class="item-name">Toxin Cleanser</span> <span class="item-tags">(Muscle, Weight Loss, Vitality)</span></p>
    <p class="item-desc">Vanilla Protein, Kale, Pear, Banana, Pineapple, Chia Seeds, Water, Ice</p>
  </div>
  <div class="menu-item super" style="top:494px;">
    <p><span class="item-name">Morning Glory</span> <span class="item-tags">(Muscle, Weight Loss, Vitality)</span></p>
    <p class="item-desc">Vanilla Protein, Blueberries, Goji Berries, Walnuts, Manuka Honey, Avocado, Coconut Water, Ice</p>
  </div>

  <!-- Kids -->
  <svg class="abs kids-blob" width="1200" height="848" viewBox="0 0 1200 848" aria-hidden="true">
    <path fill="#7dc243" d="M540 848 C548 740 610 655 720 622 C800 598 880 600 948 618 C1020 596 1110 606 1170 652 C1188 666 1196 678 1200 690 L1200 848 Z"/>
    <circle cx="998" cy="586" r="14" fill="#7dc243"/>
  </svg>
  <h2 class="section-title kids-title">For kids</h2>
  <p class="abs kids-price">$3.95</p>
  <div class="dots kids-dots"></div>

  <div class="kid" style="left:630px;top:696px;">
    <p class="item-name">Chocolate</p>
    <p class="item-desc">Low Fat Milk, Cacao Nibs, Chia Seeds</p>
  </div>
  <div class="kid" style="left:630px;top:761px;">
    <p class="item-name">Strawberry</p>
    <p class="item-desc">Low Fat Milk, Strawberries, Goji Berries</p>
  </div>
  <div class="kid" style="left:897px;top:696px;">
    <p class="item-name">Banana</p>
    <p class="item-desc">Low Fat Milk, Banana, Chia Seeds</p>
  </div>
  <div class="kid" style="left:897px;top:761px;">
    <p class="item-name">Banana Choc</p>
    <p class="item-desc">Low Fat Milk, Banana, Honey, Cacao Nibs</p>
  </div>

</body>
</html>
```